Assorted Banner Ads

Create standard sized banner ads (300x250, 728x90, 160x600) using logo and create exciting ads using collateral provided and your own ideas.

```html
<!DOCTYPE html>
<html lang="en">
<head>
<meta charset="utf-8">
<title>Coral Bay Room Escape – Banner Set</title>
<link rel="stylesheet" href="https://fonts.googleapis.com/css2?family=Cinzel:wght@700;900&family=Montserrat:wght@600;700;800&family=Archivo+Black&display=swap">
<style>
  :root{
    --page:#5a4030;
    --parchment:#e4dcc2;
    --parchment-dark:#cfc4a2;
    --green:#2f8a45;
    --green-dark:#1f6b33;
    --green-light:#6fc17f;
    --ink:#1d1d1b;
    --white:#ffffff;
  }
  *{box-sizing:border-box;margin:0;padding:0}
  html,body{width:1200px;height:1200px;overflow:hidden}
  body{background:var(--page);position:relative;font-family:"Montserrat",sans-serif}
  .banner{position:absolute;overflow:hidden;box-shadow:0 6px 14px rgba(0,0,0,.45)}
  .banner svg.art{position:absolute;inset:0;width:100%;height:100%}
  .banner > *:not(svg){position:absolute}
  .leaderboard{left:43px;top:94px;width:1113px;height:137px}
  .skyscraper{left:43px;top:274px;width:224px;height:838px}
  .rectangle{left:342px;top:279px;width:664px;height:554px}

  .brand{text-align:center;color:var(--ink);font-family:"Montserrat",sans-serif;font-weight:700;line-height:1.05}
  .brand-mark{display:block;margin:0 auto 8px;background:var(--green)}
  .brand-name{display:block;letter-spacing:.08em}
  .brand-sub{display:block;letter-spacing:.2em}

  .headline-top{font-family:"Cinzel",serif;font-weight:900;color:var(--white);letter-spacing:.04em;text-shadow:2px 2px 3px rgba(0,0,0,.7);line-height:1;white-space:nowrap}
  .headline-main{font-family:"Montserrat",sans-serif;font-weight:800;color:var(--white);text-shadow:2px 3px 3px rgba(0,0,0,.75);line-height:1;white-space:nowrap}
  .tagline{font-family:"Archivo Black",sans-serif;color:var(--white);letter-spacing:.05em;text-shadow:1px 2px 2px rgba(0,0,0,.8);white-space:nowrap}
  .rooms{list-style:none;font-weight:700;color:var(--white);text-shadow:1px 1px 2px rgba(0,0,0,.85);white-space:nowrap}
  .rooms li{display:flex;align-items:center}
  .rooms li::before{content:"";display:inline-block;background:var(--green);margin-right:.4em;width:.7em;height:.7em;flex:none}
  .cta{display:flex;align-items:center;justify-content:center;font-weight:600;color:var(--ink);background:linear-gradient(var(--green-light),var(--green) 55%,var(--green-dark));border:2px solid var(--green-dark);border-radius:6px;letter-spacing:.02em;text-decoration:none}
  .url{font-weight:800;color:var(--green);text-align:center;white-space:nowrap}
</style>
</head>
<body>

<svg width="0" height="0" style="position:absolute">
  <defs>
    <linearGradient id="photo-tone" x1="0" y1="0" x2="1" y2="0.3">
      <stop offset="0" stop-color="#dcd7cb"/>
      <stop offset=".3" stop-color="#7b776a"/>
      <stop offset=".6" stop-color="#4a5156"/>
      <stop offset="1" stop-color="#2a3944"/>
    </linearGradient>
    <linearGradient id="parchment-tone" x1="0" y1="0" x2="1" y2="1">
      <stop offset="0" stop-color="#e9e2ca"/>
      <stop offset="1" stop-color="#d6cba9"/>
    </linearGradient>
  </defs>
</svg>

<!-- 728x90 leaderboard -->
<section class="banner leaderboard">
  <svg class="art" viewBox="0 0 1113 137" preserveAspectRatio="none">
    <rect width="1113" height="137" fill="url(#parchment-tone)"/>
    <path role="img" aria-label="Close-up photo of an old rusty padlock" d="M205,0 L885,0 Q821,68 885,137 L205,137 Q171,68 205,0 Z" fill="url(#photo-tone)"/>
    <path d="M197,0 Q163,68 197,137" fill="none" stroke="#2f8a45" stroke-width="9"/>
    <path d="M205,0 Q171,68 205,137" fill="none" stroke="#e8f3ea" stroke-width="3" opacity=".8"/>
    <path d="M893,0 Q829,68 893,137" fill="none" stroke="#2f8a45" stroke-width="9"/>
    <path d="M885,0 Q821,68 885,137" fill="none" stroke="#e8f3ea" stroke-width="3" opacity=".8"/>
  </svg>
  <div class="brand" style="left:12px;top:18px;width:180px">
    <span class="brand-mark" style="width:28px;height:28px"></span>
    <span class="brand-name" style="font-size:17px">CORAL BAY</span>
    <span class="brand-sub" style="font-size:10px;margin-top:3px">ROOM ESCAPE</span>
  </div>
  <div class="headline-top" style="left:229px;top:20px;font-size:30px">Can You Escape</div>
  <div class="headline-main" style="left:229px;top:54px;font-size:39px">IN 60 MINUTES?</div>
  <div class="tagline" style="left:229px;top:110px;font-size:16px">FIND CLUES!&nbsp; SOLVE PUZZLES!</div>
  <ul class="rooms" style="left:609px;top:26px;font-size:15px;line-height:22px">
    <li>The Locked Library</li>
    <li>Sunken Ship Secrets</li>
    <li>Island Prison Break</li>
    <li>Retro Dance Fever</li>
  </ul>
  <a class="cta" style="left:897px;top:46px;width:188px;height:35px;font-size:19px">ESCAPE NOW</a>
  <div class="url" style="left:880px;top:89px;width:222px;font-size:10px">www.coralbayroomescape.com</div>
</section>

<!-- 160x600 skyscraper -->
<section class="banner skyscraper">
  <svg class="art" viewBox="0 0 224 838" preserveAspectRatio="none">
    <rect width="224" height="838" fill="url(#parchment-tone)"/>
    <path role="img" aria-label="Close-up photo of an old rusty padlock" d="M0,158 Q112,268 224,158 L224,690 Q112,570 0,690 Z" fill="url(#photo-tone)"/>
    <path d="M0,150 Q112,260 224,150" fill="none" stroke="#2f8a45" stroke-width="10"/>
    <path d="M0,158 Q112,268 224,158" fill="none" stroke="#e8f3ea" stroke-width="4" opacity=".8"/>
    <path d="M0,690 Q112,570 224,690" fill="none" stroke="#e8f3ea" stroke-width="4" opacity=".8"/>
    <path d="M0,698 Q112,578 224,698" fill="none" stroke="#2f8a45" stroke-width="10"/>
  </svg>
  <div class="brand" style="left:0;top:24px;width:224px">
    <span class="brand-mark" style="width:34px;height:34px;margin-bottom:10px"></span>
    <span class="brand-name" style="font-size:22px">CORAL BAY</span>
    <span class="brand-sub" style="font-size:12px;margin-top:4px">ROOM ESCAPE</span>
  </div>
  <div class="headline-top" style="left:0;top:276px;width:224px;text-align:center;font-size:27px;line-height:35px">Can You<br>Escape</div>
  <div class="headline-main" style="left:0;top:360px;width:224px;text-align:center;font-size:36px;line-height:43px">IN 60<br>MINUTES?</div>
  <ul class="rooms" style="left:14px;top:473px;font-size:12.5px;line-height:18.5px">
    <li>The Locked Library</li>
    <li>Sunken Ship Secrets</li>
    <li>Island Prison Break</li>
    <li>Retro Dance Fever</li>
  </ul>
  <div class="tagline" style="left:0;top:565px;width:224px;text-align:center;font-size:15px;line-height:21px">FIND CLUES!<br>SOLVE PUZZLES!</div>
  <a class="cta" style="left:24px;top:743px;width:172px;height:32px;font-size:17px">ESCAPE NOW</a>
  <div class="url" style="left:0;top:787px;width:224px;font-size:8.6px">www.coralbayroomescape.com</div>
</section>

<!-- 300x250 medium rectangle -->
<section class="banner rectangle">
  <svg class="art" viewBox="0 0 664 554" preserveAspectRatio="none">
    <rect width="664" height="554" fill="url(#parchment-tone)"/>
    <path role="img" aria-label="Close-up photo of an old rusty padlock" d="M0,100 Q332,292 664,100 L664,478 Q332,436 0,478 Z" fill="url(#photo-tone)"/>
    <path d="M0,92 Q332,284 664,92" fill="none" stroke="#2f8a45" stroke-width="11"/>
    <path d="M0,100 Q332,292 664,100" fill="none" stroke="#e8f3ea" stroke-width="5" opacity=".8"/>
    <path d="M0,478 Q332,436 664,478" fill="none" stroke="#e8f3ea" stroke-width="4" opacity=".8"/>
    <path d="M0,486 Q332,444 664,486" fill="none" stroke="#2f8a45" stroke-width="10"/>
  </svg>
  <div class="brand" style="left:0;top:28px;width:664px">
    <span class="brand-mark" style="width:40px;height:40px;margin-bottom:16px"></span>
    <span class="brand-name" style="font-size:25px">CORAL BAY</span>
    <span class="brand-sub" style="font-size:14px;margin-top:5px">ROOM ESCAPE</span>
  </div>
  <div class="headline-top" style="left:0;top:218px;width:664px;text-align:center;font-size:44px">Can You Escape</div>
  <div class="headline-main" style="left:0;top:268px;width:664px;text-align:center;font-size:56px">IN 60 MINUTES?</div>
  <ul class="rooms" style="left:78px;top:346px;font-size:17px;line-height:23px">
    <li>The Locked Library</li>
    <li>Sunken Ship Secrets</li>
  </ul>
  <ul class="rooms" style="left:366px;top:346px;font-size:17px;line-height:23px">
    <li>Island Prison Break</li>
    <li>Retro Dance Fever</li>
  </ul>
  <div class="tagline" style="left:0;top:403px;width:664px;text-align:center;font-size:19px">FIND CLUES! SOLVE PUZZLES!</div>
  <a class="cta" style="left:191px;top:445px;width:272px;height:50px;font-size:26px">ESCAPE NOW</a>
  <div class="url" style="left:0;top:505px;width:664px;font-size:24px">www.coralbayroomescape.com</div>
</section>

</body>
</html>
```